Vornel Technologies business card design

We need a business card designed with our new logo. it would be great if the card could communicate it is a technology based company.

Target Market(s)

system integrators

Industry/Entity Type

technology, IOT

Contact Information for Business Card

Name, designation, Address, telephone number, email address

Requirements
Must have
• logo and company name
Nice to have
• something to do with technology

```html
<!DOCTYPE html>
<html lang="en">
<head>
<meta charset="utf-8">
<title>Vornel Technologies – Business Card</title>
<link href="https://fonts.googleapis.com/css2?family=Roboto:wght@400;500&display=swap" rel="stylesheet">
<style>
  :root {
    --stage: #2a2a2a;
    --card-front: #3a3a3b;
    --card-back: #3d3d3e;
    --ink-light: #f2f2f2;
    --ink-soft: #d8d8d8;
    --accent: #f7941d;
  }
  * { box-sizing: border-box; margin: 0; padding: 0; }
  html, body {
    width: 1200px; height: 801px; overflow: hidden;
    background: var(--stage);
    font-family: "Roboto", Arial, sans-serif;
  }
  .stage {
    position: relative; width: 1200px; height: 801px;
    display: flex; justify-content: center; align-items: center; gap: 40px;
  }
  .card {
    position: relative; width: 300px; height: 520px;
  }
  .card--front { background: var(--card-front); }
  .card--back { background: var(--card-back); }

  .brand {
    position: absolute; top: 54px; left: 36px;
    display: flex; align-items: center; gap: 10px;
    color: var(--ink-light); font-weight: 500; font-size: 15px;
    letter-spacing: 1.5px; text-transform: uppercase;
  }
  .brand__square { width: 16px; height: 16px; background: var(--accent); }

  .person {
    position: absolute; right: 30px; bottom: 150px; text-align: right;
  }
  .person__name {
    color: var(--ink-light); font-size: 22px; font-weight: 400; letter-spacing: 0.5px;
  }
  .person__title {
    color: var(--accent); font-size: 13px; margin-top: 2px;
  }
  .contact {
    position: absolute; right: 22px; bottom: 52px; list-style: none;
  }
  .contact__item {
    display: flex; justify-content: flex-end; align-items: center; gap: 10px;
    color: var(--ink-soft); font-size: 12px; line-height: 22px;
  }
  .contact__icon { width: 12px; height: 12px; fill: var(--accent); }

  .wordmark {
    position: absolute; left: 50%; top: 50%;
    transform: translate(-50%, -50%) rotate(90deg);
    display: flex; align-items: center; gap: 14px;
    white-space: nowrap;
  }
  .wordmark__square { width: 26px; height: 26px; background: var(--accent); }
  .wordmark__name {
    color: var(--ink-light); font-weight: 500; font-size: 30px;
    letter-spacing: 4px; text-transform: uppercase; line-height: 1.15;
  }
</style>
</head>
<body>
<main class="stage">
  <section class="card card--front" aria-label="Card front">
    <div class="brand"><span class="brand__square"></span>Vornel Technologies</div>
    <div class="person">
      <p class="person__name">DANIEL REYES</p>
      <p class="person__title">Founder &amp; CEO</p>
    </div>
    <ul class="contact">
      <li class="contact__item">(555) 014-2387
        <svg class="contact__icon" viewBox="0 0 24 24"><path d="M6.6 10.8a15 15 0 0 0 6.6 6.6l2.2-2.2a1 1 0 0 1 1-.25 11.4 11.4 0 0 0 3.6.6 1 1 0 0 1 1 1V20a1 1 0 0 1-1 1A17 17 0 0 1 3 4a1 1 0 0 1 1-1h3.5a1 1 0 0 1 1 1c0 1.25.2 2.45.6 3.6a1 1 0 0 1-.25 1z"/></svg>
      </li>
      <li class="contact__item">daniel@vorneltechnologies.com
        <svg class="contact__icon" viewBox="0 0 24 24"><path d="M2 5h20v14H2z M2 5l10 8 10-8" fill="none" stroke="#f7941d" stroke-width="2.4"/></svg>
      </li>
      <li class="contact__item">vorneltechnologies.com
        <svg class="contact__icon" viewBox="0 0 24 24"><circle cx="12" cy="12" r="10" fill="none" stroke="#f7941d" stroke-width="2.4"/><path d="M2 12h20M12 2c3 3 3 17 0 20M12 2c-3 3-3 17 0 20" fill="none" stroke="#f7941d" stroke-width="1.8"/></svg>
      </li>
    </ul>
  </section>

  <section class="card card--back" aria-label="Card back">
    <div class="wordmark">
      <span class="wordmark__square"></span>
      <span class="wordmark__name">Vornel<br>Technologies</span>
    </div>
  </section>
</main>
</body>
</html>
```